Fernhollow Ridge Farms
letterhead, envelope and business cards
Fernhollow Ridge Farms -
Creative Brief
Traditional
Tessa Harlan
3157 W Birch Mill Road Quillmere, MO 68437
sales@fernhollowridgefarms.example
www.fernhollowridgefarms.example

```html
<!DOCTYPE html>
<html lang="en">
<head>
<meta charset="utf-8">
<title>Fernhollow Ridge Farms – Stationery</title>
<link rel="stylesheet" href="https://fonts.googleapis.com/css2?family=Crimson+Text:wght@600&display=swap">
<style>
  :root {
    --brown: #4f2b15;
    --brown-soft: #6b3f22;
    --cream: #e9dccb;
    --cream-light: #f3ebe0;
    --paper: #ffffff;
    --edge: #c9c9c9;
    --bg: #ffffff;
  }
  html, body {
    margin: 0;
    padding: 0;
    overflow: hidden;
    background: var(--bg);
  }
  .canvas {
    position: relative;
    width: 1200px;
    height: 754px;
    overflow: hidden;
    background: var(--bg);
    font-family: "Crimson Text", Georgia, serif;
    font-weight: 600;
    color: var(--brown);
  }
  .sheet {
    position: absolute;
    background: var(--paper);
    border: 1px solid var(--edge);
    box-sizing: border-box;
    overflow: hidden;
  }
  .brand-name {
    position: absolute;
    text-align: center;
    line-height: 0.95;
    color: var(--brown);
    white-space: nowrap;
  }
  .brand-name span { display: block; }
  .brand-name .dot {
    display: inline-block;
    border-radius: 50%;
    background: currentColor;
  }
  .scene-art {
    position: absolute;
    background: linear-gradient(180deg, rgba(233,220,203,0) 0%, var(--cream-light) 35%, var(--cream) 100%);
  }
  .band { position: absolute; left: 0; display: block; }

  /* Letterhead */
  .letterhead { left: 53px; top: 53px; width: 487px; height: 643px; }
  .letterhead .brand-name { left: 0; right: 0; top: 30px; font-size: 30px; }
  .letterhead .brand-name .dot { width: 10px; height: 10px; margin-bottom: 6px; }
  .letterhead .scene-art { left: 20px; right: 20px; bottom: 34px; height: 92px; }
  .letterhead .band { bottom: 0; width: 487px; height: 52px; }
  .letterhead .address {
    position: absolute; left: 0; right: 0; bottom: 14px;
    text-align: center; font-size: 9px; line-height: 1.35; color: var(--cream-light);
  }

  /* Business cards */
  .card { top: 91px; width: 182px; height: 104px; }
  .card-front { left: 617px; }
  .card-back { left: 812px; background: var(--brown); border-color: var(--brown); }
  .card-front .brand-name { left: 0; right: 0; top: 10px; font-size: 12px; }
  .card-front .holder {
    position: absolute; left: 0; right: 0; top: 46px;
    text-align: center; font-size: 8px; color: var(--brown);
  }
  .card-front .details {
    position: absolute; left: 0; right: 0; top: 58px;
    text-align: center; font-size: 4.5px; line-height: 1.4; color: var(--brown-soft);
  }
  .card-front .scene-art { left: 8px; right: 8px; bottom: 10px; height: 26px; }
  .card-front .band { bottom: 0; width: 182px; height: 12px; }
  .card-back .brand-name { left: 0; right: 0; top: 28px; font-size: 18px; color: var(--paper); }
  .card-back .brand-name .dot { width: 5px; height: 5px; margin-bottom: 3px; }
  .card-back .web {
    position: absolute; left: 0; right: 0; bottom: 10px;
    text-align: center; font-size: 6px; letter-spacing: 0.5px; color: var(--cream);
  }

  /* Envelope back */
  .envelope-back { left: 559px; top: 233px; width: 610px; height: 259px; }
  .envelope-back .flap {
    position: absolute; left: 0; top: 0; width: 100%; height: 43px;
    background: var(--brown);
  }
  .envelope-back .web {
    position: absolute; left: 0; right: 0; top: 13px;
    text-align: center; font-size: 14px; letter-spacing: 3px; color: var(--cream-light);
  }

  /* Envelope front */
  .envelope-front { left: 614px; top: 384px; width: 555px; height: 302px; }
  .envelope-front .brand-name { left: 22px; top: 88px; font-size: 18px; text-align: left; }
  .envelope-front .brand-name .dot { width: 6px; height: 6px; margin-bottom: 3px; }
  .envelope-front .address {
    position: absolute; left: 28px; top: 150px;
    font-size: 8px; line-height: 1.4; color: var(--brown);
  }
  .envelope-front .scene-art { left: 226px; right: 10px; bottom: 6px; height: 82px; }
</style>
</head>
<body>
<div class="canvas">

  <section class="sheet letterhead" aria-label="Letterhead">
    <div class="brand-name"><span class="dot"></span><span>Fernhollow</span><span>Ridge Farms</span></div>
    <div class="scene-art" role="img" aria-label="Faint farm scene of ducks, a dog, grasses and swirls"></div>
    <svg class="band" viewBox="0 0 487 52" preserveAspectRatio="none" aria-hidden="true">
      <path d="M0 20 Q243 -6 487 20 L487 52 L0 52 Z" fill="var(--brown)"/>
    </svg>
    <div class="address">3157 W Birch Mill Road, Quillmere, MO 68437<br>Phone: (555) 555-0142</div>
  </section>

  <section class="sheet card card-front" aria-label="Business card front">
    <div class="brand-name"><span>Fernhollow</span><span>Ridge Farms</span></div>
    <div class="holder">Tessa Harlan</div>
    <div class="details">3157 W Birch Mill Road, Quillmere, MO 68437<br>sales@fernhollowridgefarms.example</div>
    <div class="scene-art" role="img" aria-label="Faint farm scene of ducks and a dog"></div>
    <svg class="band" viewBox="0 0 182 12" preserveAspectRatio="none" aria-hidden="true">
      <path d="M0 5 Q91 -2 182 5 L182 12 L0 12 Z" fill="var(--brown)"/>
    </svg>
  </section>

  <section class="sheet card card-back" aria-label="Business card back">
    <div class="brand-name"><span class="dot"></span><span>Fernhollow</span><span>Ridge Farms</span></div>
    <div class="web">www.fernhollowridgefarms.example</div>
  </section>

  <section class="sheet envelope-back" aria-label="Envelope back">
    <div class="flap"></div>
    <div class="web">www.FernhollowRidgeFarms.example</div>
  </section>

  <section class="sheet envelope-front" aria-label="Envelope front">
    <div class="brand-name"><span class="dot"></span><span>Fernhollow</span><span>Ridge Farms</span></div>
    <div class="address">3157 W Birch Mill Road<br>Quillmere, MO 68437</div>
    <div class="scene-art" role="img" aria-label="Faint farm scene of ducks, a dog and swirls"></div>
  </section>

</div>
</body>
</html>
```